Weather of the Heart Is the Ledger A Novel by Carl Whitby and Martin Holloway

Weather of the Heart Is the Ledger is a business novel about leadership, follower-ship, resilience, and insight.
It follows a high-performing executive whose conventional management tools and techniques stop working during a professional crisis. His transformation does not come from new strategies or tactics, but from a fundamentally different understanding of how mindset shapes performance, decision-making, leadership and follower-ship. Through the course of the book, the executive, his team, and his customers realize that “State of Mind” (healthy psychological functioning) is the horsepower that drives business and life.
This is not a self-help book, textbook, or memoir. It is thoughtful business fiction with philosophical depth.

Introduction/Preface for the novel:
We wrote this book because something profound changed the way we live, work, and lead. Over the course of several decades - across boardrooms, high-stakes corporate challenges, private practice, and moments of quiet personal insight - we began to see a deeper truth about the human experience. It was a truth that, once seen, dramatically improved the quality of our lives, and the lives of the people with whom we worked.
That truth comes from understanding the Three Principles of Mind, Consciousness, and Thought, as discovered and first articulated by the philosopher and theosopher, Edwin Thorley. Though simple, these Principles point to something universally powerful—how all people experience life from the inside out. When understood, they reveal a level of clarity, resilience, and well-being that can transform not only individuals, but entire organizations.
At first, we tried to write a traditional business book—a primer designed to share how understanding the Principles can lead to more grounded, wise, and effective leadership—without the need for techniques or tools. But as we wrote, we found ourselves returning again and again to stories. Real stories. Composite stories. Fictional ones. We realized that the best way to share this understanding wasn’t through frameworks or prescriptive advice. It was through story.
So, we created one big story.
This novel is the result. Though fictional, it is inspired by real patterns, real shifts, and real struggles we’ve lived through and witnessed over decades of work, together and separately. The characters are inventions, but their experiences are familiar. We’ve watched people just like them transform—from confusion to clarity, from fear to resilience, from burnout to wisdom.
Our hope is that this book moves you—not just as a story, but as an experience. We believe that the ideas woven into Owen Castell’s journey can help anyone live with greater ease, purpose, and peace of mind. Whether you lead a Fortune 500 company or a family of five, what’s offered here is for you.
And if something in this story helps you see your own life with fresh eyes, then the book has done its job.
Welcome to the journey.
—Carl & Martin

Target Market(s)

• Senior leaders, executives, and high-potential managers • Business professionals experiencing pressure, burnout, or diminishing returns from traditional leadership approaches • Leadership coaches and organizational consultants • Readers of intelligent, reflective business fiction or non-business people who are interested in what makes people tick — and achieve their highest potential Tone should appeal to serious, experienced professionals, not beginners or hype-seekers.

Industry/Entity Type

• Business / Leadership / Psychology • Business Fiction • Leadership Novel

Font styles to use
Serif

Colors
0054AA
0677BA
7BADD7
CADEEF
E8F1F8

Requirements
Must have
• We are looking for metaphorical representations of: • A fork in the road • A deviation from the conventional path (that makes all the difference) • One element choosing a different direction—not running away, not rebelling, just seeing differently Think quiet insight, not drama. Must-Haves • Clear, legible title at thumbnail size • A visual metaphor for choice or alternate thinking • Professional, credible aesthetic • Obvious that this is fiction (a novel), not a textbook • Clean typography (no clutter)
Nice to have
• • A sense of motion or transition • Minimalist or restrained color palette • One accent element that signifies insight or departure from convention • Timeless design (should still feel current in 5 or 10 years)
Should not have
• • Literal business clichés (gears, ladders, chess pieces, lightbulbs, compasses, eagles) • Stock-photo people in suits • “Hero CEO” imagery • Overly mystical or “woo-woo” visuals • Aggressive, macho, or hustle-culture tone • Anything cartoonish or silly

```html
<!DOCTYPE html>
<html lang="en">
<head>
<meta charset="utf-8">
<title>Weather of the Heart Is the Ledger — a novel</title>
<link rel="stylesheet" href="https://fonts.googleapis.com/css2?family=Playfair+Display:ital,wght@0,600;0,700;1,400&display=swap">
<style>
  :root {
    --blue-deep: #0054AA;
    --blue-mid: #0677BA;
    --blue-soft: #7BADD7;
    --blue-pale: #CADEEF;
    --blue-mist: #E8F1F8;
    --navy-shadow: #003a78;
    --white: #ffffff;
  }
  html, body {
    margin: 0;
    padding: 0;
    overflow: hidden;
  }
  .cover {
    position: relative;
    width: 800px;
    height: 1200px;
    overflow: hidden;
    background: radial-gradient(circle at 50% 38%, var(--blue-soft), #6d9fcb);
  }
  .figure-photo {
    position: absolute;
    left: 0;
    top: 0;
  }
  .fork-path {
    position: absolute;
    left: 0;
    top: 0;
  }
  .title-disc {
    position: absolute;
    left: 150px;
    top: 144px;
    width: 508px;
    height: 508px;
    border-radius: 50%;
    background: radial-gradient(circle at 42% 38%, var(--white) 0%, var(--blue-mist) 55%, var(--blue-pale) 100%);
  }
  .title {
    position: absolute;
    left: 150px;
    width: 508px;
    top: 292px;
    margin: 0;
    text-align: center;
    font-family: "Playfair Display", serif;
    font-weight: 700;
    color: var(--blue-deep);
    text-transform: uppercase;
    line-height: 1;
  }
  .title-line {
    display: block;
  }
  .title-line--large {
    font-size: 64px;
    line-height: 1.12;
    letter-spacing: 1px;
  }
  .title-line--small {
    font-size: 38px;
    font-weight: 600;
    margin-top: 22px;
    letter-spacing: 2px;
    color: var(--blue-mid);
  }
  .genre {
    position: absolute;
    left: 566px;
    top: 664px;
    margin: 0;
    font-family: "Playfair Display", serif;
    font-style: italic;
    font-weight: 400;
    font-size: 40px;
    color: var(--white);
  }
  .authors {
    position: absolute;
    left: 0;
    width: 800px;
    top: 1050px;
    margin: 0;
    text-align: center;
    font-family: "Playfair Display", serif;
    font-weight: 600;
    font-size: 32px;
    line-height: 1.25;
    letter-spacing: 2px;
    color: var(--white);
    text-transform: uppercase;
  }
  .authors span {
    display: block;
  }
</style>
</head>
<body>
  <main class="cover">
    <svg class="figure-photo" width="800" height="1200" viewBox="0 0 800 1200" role="img" aria-label="Photograph of a man in a dark suit fastening his jacket button, his head hidden behind the title disc">
      <defs>
        <linearGradient id="suitTone" x1="0" y1="0" x2="0" y2="1">
          <stop offset="0" stop-color="var(--blue-deep)"/>
          <stop offset="1" stop-color="var(--navy-shadow)"/>
        </linearGradient>
      </defs>
      <path d="M160 1200 L160 660 Q160 590 250 570 L550 570 Q650 590 655 660 L655 1200 Z" fill="url(#suitTone)"/>
    </svg>

    <svg class="fork-path" width="800" height="1200" viewBox="0 0 800 1200" aria-hidden="true">
      <path d="M400 1030 L400 652" fill="none" stroke="var(--blue-soft)" stroke-width="4" stroke-linecap="round"/>
      <path d="M400 860 C400 780 470 740 548 712" fill="none" stroke="var(--blue-mist)" stroke-width="4" stroke-linecap="round"/>
      <circle cx="556" cy="709" r="6" fill="var(--white)"/>
    </svg>

    <div class="title-disc"></div>

    <h1 class="title">
      <span class="title-line title-line--large">Weather of</span>
      <span class="title-line title-line--large">the Heart</span>
      <span class="title-line title-line--small">Is the Ledger</span>
    </h1>

    <p class="genre">a novel</p>

    <p class="authors">
      <span>Carl Whitby</span>
      <span>Martin Holloway</span>
    </p>
  </main>
</body>
</html>
```